Talvex Engineering Business card Design

We need to make business cards for our NDT and inspection company. The company is called Talvex Engineering. We want a professional modern feel business card. We have just completed the remaking of our website and would like to have business cards with the same feel and colours. The final design should communicate professionalism and cutting edge tech.

Target Market(s)

We sell to B2B Business clients. Our customer is an engineer or decision maker in the mechanical engineering / Oil and gas field.

Contact Information for Business Card

Please see the current business cards that we have uploaded to get the details. You can also look at our Website www.talvex-eng.example for more.

Requirements
Must have
• Less is more
Nice to have
• Less is more

```html
<!DOCTYPE html>
<html lang="en">
<head>
<meta charset="UTF-8">
<title>Talvex Engineering – Business Cards</title>
<link rel="stylesheet" href="https://fonts.googleapis.com/css2?family=Work+Sans:wght@400;500;700&display=swap">
<style>
  :root {
    --brand-red: #a81e24;
    --brand-navy: #1d3a6e;
    --text-grey: #4a4a4a;
    --card-white: #ffffff;
    --backdrop: #e9e9eb;
    --rule: #8a8a8a;
  }
  * { box-sizing: border-box; margin: 0; padding: 0; }
  html, body {
    width: 1200px; height: 900px; overflow: hidden;
    background: var(--backdrop);
    font-family: "Work Sans", Arial, sans-serif;
  }
  .sheet {
    position: relative; width: 1200px; height: 900px;
  }
  .card {
    position: absolute; left: 250px;
    width: 700px; height: 400px;
    background: var(--card-white);
    box-shadow: 0 6px 18px rgba(0,0,0,.18);
    overflow: hidden;
  }
  .card--back { top: 35px; }
  .card--front { top: 465px; }

  .card__bands { position: absolute; left: 0; bottom: 0; width: 700px; height: 46px; }
  .card__url {
    position: absolute; right: 22px; bottom: 11px;
    color: var(--card-white); font-size: 15px; font-weight: 500; letter-spacing: .3px;
  }

  .brand {
    position: absolute; display: flex; align-items: center; gap: 12px;
  }
  .brand__dot {
    width: 34px; height: 34px; border-radius: 50%;
    border: 2px solid var(--brand-red);
  }
  .brand__name {
    color: var(--brand-navy); font-size: 22px; font-weight: 700; line-height: 1.2;
  }
  .card--back .brand { left: 420px; top: 100px; width: 250px; }
  .card--front .brand { left: 55px; top: 170px; width: 270px; }

  .services {
    position: absolute; left: 40px; top: 34px;
    list-style: none; color: var(--text-grey);
    font-size: 16px; line-height: 22px;
  }
  .services li { position: relative; padding-left: 16px; }
  .services li::before {
    content: ""; position: absolute; left: 0; top: 9px;
    width: 5px; height: 5px; border-radius: 50%; background: var(--brand-red);
  }
  .services .group-start { margin-top: 16px; }

  .divider {
    position: absolute; left: 350px; top: 95px;
    width: 1px; height: 200px; background: var(--brand-navy);
  }
  .contact {
    position: absolute; left: 378px; top: 95px; color: var(--text-grey);
  }
  .contact__name { color: var(--brand-navy); font-size: 26px; font-weight: 700; }
  .contact__role { font-size: 16px; margin-top: 2px; }
  .contact__address { font-size: 16px; line-height: 23px; margin-top: 18px; font-style: normal; }
  .contact__lines { list-style: none; margin-top: 16px; font-size: 16px; line-height: 24px; }
  .contact__lines li { display: flex; align-items: center; gap: 8px; }
  .contact__lines svg { width: 14px; height: 14px; flex: none; }
</style>
</head>
<body>
<main class="sheet">

  <section class="card card--back" aria-label="Card back">
    <ul class="services">
      <li>API 653 Tank Inspections</li>
      <li>API 570 Pipeline Inspections</li>
      <li>API 510 Pressure Vessel Inspections</li>
      <li>Welding Inspection</li>
      <li>Electrical Inspection</li>
      <li>OCTG Inspections</li>
      <li>Lifting Equipment Inspections</li>
      <li class="group-start">Non-Destructive Testing</li>
      <li>UT / PT / MT / RT / VT</li>
      <li>Advanced NDT</li>
      <li>PAUT / MFL / ILI</li>
      <li class="group-start">Engineering Projects</li>
    </ul>

    <div class="brand">
      <span class="brand__dot"></span>
      <span class="brand__name">Talvex Engineering</span>
    </div>

    <svg class="card__bands" viewBox="0 0 700 46" aria-hidden="true">
      <polygon points="0,34 455,34 452,46 0,46" fill="var(--brand-red)"/>
      <polygon points="468,4 700,4 700,46 458,46" fill="var(--brand-navy)"/>
    </svg>
    <span class="card__url">www.talvex-eng.example</span>
  </section>

  <section class="card card--front" aria-label="Card front">
    <div class="brand">
      <span class="brand__dot"></span>
      <span class="brand__name">Talvex Engineering</span>
    </div>

    <div class="divider"></div>

    <div class="contact">
      <h1 class="contact__name">Jonah Wekesa</h1>
      <p class="contact__role">President</p>
      <address class="contact__address">P.O. BOX 40512-80100<br>Mombasa Kenya</address>
      <ul class="contact__lines">
        <li>
          <svg viewBox="0 0 14 14" aria-hidden="true"><path d="M3 1l2 3-1.3 1.3a8 8 0 0 0 5 5L10 9l3 2-1.2 2.2C6 13 1 8 .8 2.2z" fill="var(--brand-red)"/></svg>
          254 20 555 0142/3
        </li>
        <li>
          <svg viewBox="0 0 14 14" aria-hidden="true"><rect x="1" y="3" width="12" height="8" fill="var(--brand-red)"/><path d="M1 3l6 5 6-5" fill="none" stroke="#fff" stroke-width="1.2"/></svg>
          info@talvex-eng.example
        </li>
      </ul>
    </div>

    <svg class="card__bands" viewBox="0 0 700 46" aria-hidden="true">
      <polygon points="0,34 455,34 452,46 0,46" fill="var(--brand-red)"/>
      <polygon points="468,4 700,4 700,46 458,46" fill="var(--brand-navy)"/>
    </svg>
    <span class="card__url">www.talvex-eng.example</span>
  </section>

</main>
</body>
</html>
```